Window Cleaning Flyer targeting Shopfronts and Small Commercial Work

Single page flyer similar to the flyer targeting small commercial work and shopfronts

Please include the following text:

Brisk Pane Services delivers high quality service to suburbs all around Melbourne. From Frankston to Kalkallo, Brisk has you covered!

With over 10 years experience, Brisk specialises in providing:
- Window Cleaning: via elevated work platforms, rope access and extension poles
- Pressure Cleaning: Including chlorine treatment to prevent mould regrowth on concrete area
- Roof Gutter Cleaning: using our ladder free gutter vacuum

We pride ourselves on neat and professional presentation and vast geographical reach across Melbourne.

Our services can be completed on a frequency that meets your window cleaning needs. Whether a weekly clean or a yearly service.

Brisk Pane Services Melbourne takes care of all your window cleaning needs.

Contact Us now for free quote!

Target Market(s)

Small business and commercial building owners

Industry/Entity Type

Window Cleaning

Requirements
Must have
• Only use photos/logos provided
Should not have
• Stock phots

```html
<!DOCTYPE html>
<html lang="en">
<head>
<meta charset="utf-8">
<title>Brisk Pane Services – Flyer</title>
<link href="https://fonts.googleapis.com/css2?family=Open+Sans:wght@400;600;700;800&family=Source+Serif+4:ital,wght@0,400;0,700;1,400&display=swap" rel="stylesheet">
<style>
:root{
  --navy:#0e4f86;
  --navy-deep:#0b3f6e;
  --yellow:#f7e81a;
  --white:#ffffff;
  --stage:#c9c9c9;
  --brick-1:#8a5a44;
  --brick-2:#b08068;
  --roof:#3c3a36;
}
*{margin:0;padding:0;box-sizing:border-box}
html,body{width:869px;height:1200px;overflow:hidden;background:var(--stage)}
.flyer{position:absolute;left:42px;top:36px;width:786px;height:1118px;background:var(--navy);overflow:hidden;box-shadow:0 8px 18px rgba(0,0,0,.35);font-family:"Open Sans",sans-serif;color:var(--white)}
.hero-photo{position:absolute;left:0;top:0;width:786px;height:400px;background:linear-gradient(180deg,var(--roof) 0%,var(--roof) 12%,var(--brick-1) 13%,var(--brick-2) 55%,#9a9088 100%)}
.shapes{position:absolute;left:0;top:0}
.badge{position:absolute;left:524px;top:312px;width:180px;height:180px;text-align:center;color:var(--yellow);font-family:"Source Serif 4",serif;font-style:italic}
.badge .over{position:absolute;top:42px;width:100%;font-size:26px;line-height:1}
.badge .num{position:absolute;top:66px;width:100%;font-size:58px;line-height:1}
.badge .years{position:absolute;top:122px;width:100%;font-size:15px;line-height:1.2}
.brand{position:absolute;left:32px;top:376px;color:var(--yellow);font-weight:800}
.brand .name{font-size:70px;line-height:1;letter-spacing:1px}
.brand .sub{font-size:22px;line-height:1;margin-top:12px;letter-spacing:1.2px}
.intro{position:absolute;left:32px;top:522px;width:740px;font-size:19.5px;line-height:1.4}
.intro .hl{color:var(--yellow)}
.services-title{position:absolute;left:32px;top:602px;font-size:21px;font-weight:700;color:var(--yellow)}
.service{position:absolute;padding-left:28px;font-family:"Source Serif 4",serif}
.service .icon{position:absolute;left:0;top:3px;width:18px;height:18px}
.service h3{font-size:19px;font-weight:700;line-height:1.25}
.service p{font-size:14.5px;line-height:1.3}
.points{position:absolute;left:32px;top:856px;width:740px;list-style:none;font-size:15.5px;line-height:1.35}
.points li{position:relative;padding-left:28px;margin-bottom:10px}
.points li svg{position:absolute;left:2px;top:3px}
.contact-lead{position:absolute;left:48px;top:988px;font-family:"Source Serif 4",serif;font-size:19px}
.quote-tag{position:absolute;left:40px;top:1018px;padding:3px 8px;background:var(--yellow);color:var(--navy-deep);font-family:"Source Serif 4",serif;font-size:24px;line-height:1.3;border-radius:3px}
.phone{position:absolute;left:40px;top:1064px;display:flex;align-items:center;gap:6px;color:var(--yellow);font-weight:700;font-size:36px;line-height:1}
.contact-band{position:absolute;right:0;top:1056px}
.contact-lines{position:absolute;right:14px;top:1068px;text-align:right;color:var(--navy-deep);font-family:"Source Serif 4",serif;font-size:15.5px;line-height:1.55}
.contact-lines div{display:flex;align-items:center;justify-content:flex-end;gap:10px}
</style>
</head>
<body>
<main class="flyer">
  <div class="hero-photo" role="img" aria-label="Photo of a window cleaner using an extension pole on windows under a brick veranda"></div>

  <svg class="shapes" width="786" height="1118" viewBox="0 0 786 1118" aria-hidden="true">
    <path d="M0 330 C180 250 400 300 560 360 C650 392 730 360 786 330 L786 1118 L0 1118 Z" fill="var(--yellow)"/>
    <path d="M0 352 C180 282 400 330 560 392 C650 422 730 392 786 368 L786 1118 L0 1118 Z" fill="var(--navy)"/>
  </svg>

  <svg class="badge-star" style="position:absolute;left:524px;top:312px" width="180" height="180" viewBox="0 0 180 180" aria-hidden="true">
    <polygon fill="var(--navy)" stroke="#9bb4cc" stroke-width="3" points="90,4 101,26 121,11 124,36 148,28 142,52 168,52 154,74 177,86 156,100 171,121 146,124 150,149 126,142 120,167 101,152 90,176 79,152 60,167 54,142 30,149 34,124 9,121 24,100 3,86 26,74 12,52 38,52 32,28 56,36 59,11 79,26"/>
  </svg>
  <div class="badge">
    <div class="over">over</div>
    <div class="num">10</div>
    <div class="years">years of<br>experience</div>
  </div>

  <div class="brand">
    <div class="name">BRISK</div>
    <div class="sub">PANE SERVICES</div>
  </div>

  <p class="intro">Brisk Pane Services delivers <span class="hl">high quality service</span> to suburbs all around Melbourne. From Frankston to Kalkallo, Brisk has you covered!</p>

  <h2 class="services-title">Brisk specialises in providing:</h2>

  <div class="service" style="left:32px;top:656px">
    <svg class="icon" viewBox="0 0 18 18" aria-hidden="true"><circle cx="9" cy="9" r="9" fill="var(--yellow)"/><rect x="5" y="5" width="8" height="8" fill="none" stroke="var(--navy)" stroke-width="1.6"/></svg>
    <h3>Window Cleaning</h3>
    <p>via elevated work platforms, rope access<br>and extension poles</p>
  </div>
  <div class="service" style="left:432px;top:656px">
    <svg class="icon" viewBox="0 0 18 18" aria-hidden="true"><circle cx="9" cy="9" r="9" fill="var(--yellow)"/><path d="M5 12 H13 M6 12 V7 M12 12 V7" stroke="var(--navy)" stroke-width="1.6" fill="none"/></svg>
    <h3>Gutter Cleaning</h3>
    <p>(using our ladder free gutter vacuum)</p>
  </div>
  <div class="service" style="left:32px;top:735px">
    <svg class="icon" viewBox="0 0 18 18" aria-hidden="true"><circle cx="9" cy="9" r="9" fill="var(--yellow)"/><path d="M5 13 L13 5" stroke="var(--navy)" stroke-width="2"/></svg>
    <h3>Pressure Washing</h3>
    <p>Including chlorine treatment to prevent<br>mould regrowth on concrete area</p>
  </div>

  <ul class="points">
    <li><svg width="14" height="16" viewBox="0 0 14 16" aria-hidden="true"><polygon points="2,1 13,8 2,15" fill="var(--yellow)"/></svg>We pride ourselves on neat and professional presentation and vast geographical reach across Melbourne.</li>
    <li><svg width="14" height="16" viewBox="0 0 14 16" aria-hidden="true"><polygon points="2,1 13,8 2,15" fill="var(--yellow)"/></svg>Our services can be completed on a frequency that meets your window cleaning needs. Whether a weekly clean or a yearly service.</li>
    <li><svg width="14" height="16" viewBox="0 0 14 16" aria-hidden="true"><polygon points="2,1 13,8 2,15" fill="var(--yellow)"/></svg>Brisk Pane Services Melbourne takes care of all your window cleaning needs.</li>
  </ul>

  <p class="contact-lead">Contact the Brisk Team for an easy,</p>
  <p class="quote-tag">Get a <strong>FREE</strong> quote today!</p>
  <div class="phone">
    <svg width="32" height="32" viewBox="0 0 24 24" aria-hidden="true"><path fill="var(--yellow)" d="M6.6 10.8a15.1 15.1 0 0 0 6.6 6.6l2.2-2.2c.3-.3.7-.4 1-.2 1.1.4 2.3.6 3.6.6.6 0 1 .4 1 1V20c0 .6-.4 1-1 1A17 17 0 0 1 3 4c0-.6.4-1 1-1h3.5c.6 0 1 .4 1 1 0 1.3.2 2.5.6 3.6.1.3 0 .7-.2 1z"/></svg>
    <span>(03) 9000 4417</span>
  </div>

  <svg class="contact-band" width="390" height="62" viewBox="0 0 390 62" aria-hidden="true">
    <polygon points="0,62 24,0 44,0 20,62" fill="var(--yellow)"/>
    <polygon points="28,62 52,0 390,0 390,62" fill="var(--white)"/>
  </svg>
  <div class="contact-lines">
    <div><svg width="18" height="12" viewBox="0 0 18 12" aria-hidden="true"><rect width="18" height="12" fill="var(--navy)"/><path d="M0 0 L9 7 L18 0" stroke="var(--white)" stroke-width="1.4" fill="none"/></svg>hello@briskpane.com.au</div>
    <div><svg width="14" height="14" viewBox="0 0 14 14" aria-hidden="true"><circle cx="7" cy="7" r="6" fill="none" stroke="var(--navy)" stroke-width="1.4"/><path d="M1 7 H13 M7 1 C4 4 4 10 7 13 M7 1 C10 4 10 10 7 13" stroke="var(--navy)" stroke-width="1.2" fill="none"/></svg>www.briskpane-melbourne.com.au</div>
  </div>
</main>
</body>
</html>
```